The Lantern Hour Book Cover

Cover for Multiauthor Ebook & Paper Print Book Cover

Book Title:
The Lantern Hour : Dawn Beyond Craving

This collaborative multiauthor book is a collection of stories of recovery and rising from addiction for those looking for hope and the courage to take their own lantern hour. Whether contemplating making the first step or having completed all 12 of them, recovery from alcohol, drug, codependency, eating, sex, shame, gambling, busyness, etc is a path we will always walk.

Need extra days to review

Target Market(s)

Humans looking for guidance and words of wisdom healing from addiction of all kinds - to know they aren't alone, to provide guidance, and to give them hope. Ages 16 and up. Any Gender. International. Looking for The Lantern Hour in their recovery process and life.

Industry/Entity Type

Recovery, Addiction, Wellness

Font styles to use
Serif
Script

Colors
0054AA
0677BA
7BADD7
CADEEF
E8F1F8
FFF300
FFF600
FEFA6F
FFFEC7
FFFEE8

Requirements
Must have
• masculine and feminine elements, mostly Black & White but with some soft sunrise elements of color
Nice to have
• steps or stairs
Should not have
• anything that feels depressing, we want honest but hopeful

```html
<!DOCTYPE html>
<html lang="en">
<head>
<meta charset="utf-8">
<title>The Lantern Hour : Dawn Beyond Craving — Book Cover</title>
<link rel="stylesheet" href="https://fonts.googleapis.com/css2?family=Playfair+Display:ital,wght@1,500&family=Montserrat:ital,wght@0,700;1,900&display=swap">
<style>
  :root {
    --backdrop: #4f8fdb;
    --cover-top: #8db4ee;
    --cover-mid: #a9c6f2;
    --cover-base: #6f9fe3;
    --glow-core: #fbeff0;
    --glow-halo: rgba(246, 228, 240, 0.55);
    --ink: #283a8e;
    --spine-line: rgba(255, 255, 255, 0.35);
  }
  * { margin: 0; padding: 0; box-sizing: border-box; }
  html, body {
    width: 1200px;
    height: 1093px;
    overflow: hidden;
    background: var(--backdrop);
  }
  .canvas {
    position: relative;
    width: 1200px;
    height: 1093px;
  }
  .book-cover {
    position: absolute;
    left: 235px;
    top: 30px;
    width: 730px;
    height: 1033px;
    overflow: hidden;
    background: var(--cover-mid);
  }
  .cover-art {
    position: absolute;
    inset: 0;
    background:
      radial-gradient(circle at 50% 47%, var(--glow-core) 0%, var(--glow-halo) 14%, rgba(200, 218, 246, 0) 34%),
      linear-gradient(180deg, var(--cover-top) 0%, var(--cover-mid) 45%, var(--cover-base) 100%);
  }
  .spine-edge {
    position: absolute;
    left: 34px;
    top: 0;
    bottom: 0;
    width: 1px;
    background: var(--spine-line);
  }
  .title-block {
    position: absolute;
    left: 0;
    right: 0;
    top: 540px;
    text-align: center;
    color: var(--ink);
  }
  .title-lead {
    display: block;
    font-family: "Playfair Display", Georgia, serif;
    font-style: italic;
    font-weight: 500;
    font-size: 84px;
    line-height: 1;
    letter-spacing: -1px;
    margin-left: 40px;
  }
  .title-main {
    display: block;
    font-family: "Montserrat", Arial, sans-serif;
    font-style: italic;
    font-weight: 900;
    font-size: 98px;
    line-height: 0.98;
    letter-spacing: -3px;
    text-transform: uppercase;
    margin-top: 6px;
  }
  .subtitle {
    position: absolute;
    left: 0;
    right: 0;
    top: 905px;
    text-align: center;
    font-family: "Montserrat", Arial, sans-serif;
    font-weight: 700;
    font-size: 25px;
    letter-spacing: 0.5px;
    color: var(--ink);
    text-transform: uppercase;
  }
</style>
</head>
<body>
  <main class="canvas">
    <section class="book-cover">
      <div class="cover-art" role="img" aria-label="Illustration of a glowing arched doorway at the top of a long staircase, bathed in soft blue and warm light"></div>
      <div class="spine-edge"></div>
      <h1 class="title-block">
        <span class="title-lead">The</span>
        <span class="title-main">Lantern<br>Hour</span>
      </h1>
      <p class="subtitle">Dawn Beyond Craving</p>
    </section>
  </main>
</body>
</html>
```